Business card for an e-commerce/social networking website
Bazorin
Simple
Yousef Karim AlShehhi
Chief Financial Officer
Palm Crest Isle, Orchid Court Apt 418 Abu Dhabi, United Arab Emirates
1-800-BAZORIN
alshehhi@bazorin.ae
www.Bazorin.ae
the card be contemporary. easy on the eye. not cluttered.
the single "B" in the box.

```html
<!DOCTYPE html>
<html lang="en">
<head>
<meta charset="utf-8">
<title>Bazorin Business Card</title>
<link href="https://fonts.googleapis.com/css2?family=Open+Sans:wght@400;600;700&display=swap" rel="stylesheet">
<style>
  :root {
    --backdrop: #eceef1;
    --card: #ffffff;
    --brand-blue: #2a8fd8;
    --ink: #4a4f55;
    --ink-soft: #7a8088;
    --box-edge: #d9dde2;
  }
  * { margin: 0; padding: 0; box-sizing: border-box; }
  html, body {
    width: 1200px; height: 629px; overflow: hidden;
    background: var(--backdrop);
    font-family: "Open Sans", Arial, sans-serif;
  }
  .stage {
    width: 1200px; height: 629px;
    display: flex; align-items: center; justify-content: center; gap: 60px;
  }
  .card {
    position: relative;
    width: 500px; height: 286px;
    background: var(--card);
    box-shadow: 0 6px 22px rgba(0,0,0,.12);
  }
  .logo-box {
    position: absolute;
    display: flex; align-items: center; justify-content: center; gap: 10px;
    background: var(--card);
    border: 1px solid var(--box-edge);
    border-radius: 12px;
    box-shadow: 0 3px 8px rgba(0,0,0,.12);
  }
  .logo-dot {
    width: 18px; height: 18px; border-radius: 50%;
    background: var(--brand-blue);
  }
  .logo-name {
    font-weight: 700; color: var(--brand-blue); letter-spacing: -.5px;
  }
  .card-front .logo-box {
    left: 115px; top: 98px; width: 270px; height: 90px;
  }
  .card-front .logo-name { font-size: 44px; }

  .card-back .logo-box {
    left: 28px; top: 28px; width: 444px; height: 74px;
  }
  .card-back .logo-name { font-size: 40px; }
  .card-back .logo-dot { width: 16px; height: 16px; }

  .person {
    position: absolute; left: 34px; top: 120px;
  }
  .person-name {
    font-size: 13px; font-weight: 700; color: var(--brand-blue);
  }
  .person-title {
    font-size: 11px; color: var(--ink-soft); margin-top: 2px;
  }
  .address {
    position: absolute; left: 34px; bottom: 30px;
    font-size: 10.5px; line-height: 1.5; color: var(--ink);
  }
  .contact-list {
    position: absolute; left: 290px; top: 122px;
    list-style: none;
  }
  .contact-list li {
    display: flex; align-items: center; gap: 8px;
    font-size: 10.5px; color: var(--ink); height: 21px;
  }
  .contact-list svg { width: 13px; height: 13px; flex: none; }
</style>
</head>
<body>
<main class="stage">
  <section class="card card-front">
    <div class="logo-box">
      <span class="logo-dot"></span>
      <span class="logo-name">Bazorin</span>
    </div>
  </section>

  <section class="card card-back">
    <div class="logo-box">
      <span class="logo-dot"></span>
      <span class="logo-name">Bazorin</span>
    </div>

    <div class="person">
      <p class="person-name">Yousef Karim AlShehhi</p>
      <p class="person-title">Chief Financial Officer</p>
    </div>

    <address class="address">
      Palm Crest Isle, Orchid Court Apt 418<br>
      Abu Dhabi, United Arab Emirates
    </address>

    <ul class="contact-list">
      <li><svg viewBox="0 0 14 14"><circle cx="7" cy="7" r="7" fill="#2a8fd8"/><path d="M4.6 3.8l1.3 1.3-.7.9c.5 1 1.3 1.8 2.3 2.3l.9-.7 1.3 1.3-.9 1.1c-2.4-.4-4.4-2.4-4.8-4.8z" fill="#fff"/></svg>1-800-BAZORIN</li>
      <li><svg viewBox="0 0 14 14"><circle cx="7" cy="7" r="7" fill="#2a8fd8"/><rect x="5" y="3.2" width="4" height="7.6" rx=".8" fill="#fff"/></svg>+971 50 412 7730</li>
      <li><svg viewBox="0 0 14 14"><circle cx="7" cy="7" r="7" fill="#2a8fd8"/><path d="M4.6 3.8l1.3 1.3-.7.9c.5 1 1.3 1.8 2.3 2.3l.9-.7 1.3 1.3-.9 1.1c-2.4-.4-4.4-2.4-4.8-4.8z" fill="#fff"/></svg>+971 2 618 4402</li>
      <li><svg viewBox="0 0 14 14"><circle cx="7" cy="7" r="7" fill="#2a8fd8"/><rect x="4" y="5" width="6" height="4.5" fill="#fff"/><rect x="5" y="3.2" width="4" height="1.4" fill="#fff"/></svg>+971 2 618 4403</li>
      <li><svg viewBox="0 0 14 14"><circle cx="7" cy="7" r="7" fill="#2a8fd8"/><rect x="3.6" y="4.6" width="6.8" height="4.8" fill="#fff"/><path d="M3.6 4.6L7 7.4l3.4-2.8" stroke="#2a8fd8" stroke-width=".8" fill="none"/></svg>alshehhi@bazorin.ae</li>
      <li><svg viewBox="0 0 14 14"><circle cx="7" cy="7" r="7" fill="#2a8fd8"/><circle cx="7" cy="7" r="3.4" fill="none" stroke="#fff" stroke-width=".9"/><path d="M3.6 7h6.8M7 3.6v6.8" stroke="#fff" stroke-width=".8"/></svg>www.Bazorin.ae</li>
    </ul>
  </section>
</main>
</body>
</html>
```